Update Powerpoint Presentation

We need to update the existing Powerpoint presentation to make it look more professional, less words and get the message across to potential clients. Our clients are banks and lenders in Australia.
Reason: To give the designers more time to come up with designs
Reason: I am looking for a design that is more innovative and doesn't just re-create what I gave. This presentation is only an example of what I would like I am keen to find a presentation that takes it to the next level.

```html
<!DOCTYPE html>
<html lang="en">
<head>
<meta charset="utf-8">
<title>Northgate Loan Services – Presentation to XYZ Lender</title>
<link rel="stylesheet" href="https://fonts.googleapis.com/css2?family=Source+Sans+3:wght@400;600;700&family=Tinos:ital,wght@1,700&display=swap">
<style>
:root{
  --bg:#e9e6e1;
  --slide-edge:#d9d9dc;
  --navy:#2b3a8f;
  --sky:#33b0e3;
  --sky-dark:#1e8fc4;
  --ink:#222;
  --pill-top:#ffffff;
  --pill-bottom:#9c9ad6;
  --grey-title:#6b6b6b;
}
*{box-sizing:border-box;margin:0;padding:0}
html,body{width:1200px;height:606px;overflow:hidden;background:var(--bg)}
body{position:relative;font-family:"Source Sans 3",Arial,sans-serif;color:var(--ink)}
.slide{position:absolute;width:380px;height:284px;background:linear-gradient(180deg,#fff 0%,#f1f1f3 100%);border:1px solid var(--slide-edge);box-shadow:0 2px 5px rgba(0,0,0,.12);overflow:hidden}
.slide--title{left:216px;top:12px}
.slide--messages{left:622px;top:12px}
.slide--intro{left:6px;top:312px}
.slide--services{left:414px;top:312px}
.slide--closing{left:810px;top:312px}

.company-name{position:absolute;color:var(--navy);font-weight:600;line-height:1.05;text-align:center}
.pill{position:absolute;border:1.5px solid #222;background:linear-gradient(180deg,var(--pill-top) 0%,var(--pill-bottom) 100%);color:#222;text-align:center;display:flex;align-items:center;justify-content:center;line-height:1.1}
.footer-url{position:absolute;top:266px;left:0;right:0;text-align:center;font-size:9px;letter-spacing:2px;color:#333}
.confidential{position:absolute;font-size:5.5px;color:#333}

/* title slide */
.slide--title .company-name{top:40px;left:0;right:0;font-size:36px}
.presentation-pill{left:85px;top:154px;width:196px;height:31px;border-radius:16px;font-size:16px}
.client{position:absolute;top:197px;left:0;right:0;text-align:center;font-size:11px;line-height:21px}

/* key messages */
.heading-pill{left:188px;top:18px;width:98px;height:20px;border-radius:10px;font-size:12px}
.msg-label{left:15px;width:66px;border-radius:10px;font-size:7.5px;font-weight:700}
.msg-box{position:absolute;left:122px;width:236px;background:var(--sky);border:1px solid var(--sky-dark);color:#fff;font-size:4.8px;line-height:1.4;text-align:center;padding:3px 12px;border-radius:11px;display:flex;flex-direction:column;justify-content:center}
.msg-box b{display:block;color:var(--navy);font-weight:700}
.msg-box--opportunities{border-radius:36px;padding:6px 18px}
.slide--messages .confidential{top:272px;left:0;right:0;text-align:center}

/* shared section header */
.section-pill{left:11px;top:14px;height:21px;border-radius:11px;font-size:12.5px;padding:0 10px}
.corner-name{top:12px;width:100px;font-size:11px}
.col-title{position:absolute;top:74px;font-size:8.5px;font-weight:700;color:var(--navy);border-bottom:1px solid var(--navy);padding-bottom:2px}

/* intro */
.intro-text{position:absolute;left:11px;top:96px;width:166px;font-size:5.9px;line-height:1.42}
.intro-text p{margin-bottom:6px}
.map-area{position:absolute;left:198px;top:100px;width:168px;height:164px;border-radius:38% 30% 34% 44%;background:linear-gradient(135deg,#b879c6 0%,#f4cfa9 72%)}
.slide--intro .confidential{left:11px;top:273px}

/* services */
.intro-note{position:absolute;left:14px;top:46px;width:344px;font-size:5.6px;line-height:1.55}
.flow{position:absolute;left:14px;height:27px;display:flex;background:var(--sky);border-radius:14px}
.flow span{flex:1;color:#fff;font-size:5px;text-align:center;display:flex;align-items:center;justify-content:center;border-right:1px solid #fff;line-height:1.1;padding:0 2px}
.flow span:last-child{border-right:none}
.flow--loans{top:82px;width:342px}
.flow--discharges{top:182px;width:302px}
.flow-notes{position:absolute;left:14px;display:flex}
.flow-notes ul{flex:1;list-style:disc;padding-left:8px;font-size:4.3px;line-height:1.3;padding-right:2px}
.flow-notes--loans{top:112px;width:342px}
.flow-notes--discharges{top:216px;width:302px}
.flow-tag{height:20px;border-radius:10px;font-size:7px;font-weight:600}
.slide--services .confidential{left:14px;top:277px}

/* closing */
.slide--closing .company-name{top:54px;left:0;right:0;font-size:34px}
.thanks{position:absolute;top:154px;left:0;right:0;text-align:center;font-family:"Tinos",serif;font-style:italic;font-weight:700;font-size:20px;line-height:1.12;color:var(--grey-title)}
.contact{position:absolute;top:219px;left:0;right:0;text-align:center;font-size:9px;line-height:1.45;color:#333}
</style>
</head>
<body>

<section class="slide slide--title">
  <div class="company-name">Northgate<br>Loan Services</div>
  <div class="pill presentation-pill">PRESENTATION TO</div>
  <div class="client">XYZ Lender<br>June 2013</div>
  <div class="footer-url">www.northgatels.com</div>
</section>

<section class="slide slide--messages">
  <div class="pill heading-pill">KEY MESSAGES</div>

  <div class="pill msg-label" style="top:54px;height:19px">XYZ Lender</div>
  <div class="msg-box" style="top:53px;height:22px">XYZ Lender currently outsources processing of new loans and discharges and is looking at new models to lift its service through innovation and technology enhancements.</div>

  <div class="pill msg-label" style="top:90px;height:19px">NLS</div>
  <div class="msg-box" style="top:81px;height:40px">NLS is a leading outsourced mortgage document and settlement business in Australia. It is backed by a global title and settlement group that serves lenders, buyers and sellers across several markets through its own offices and partners.</div>

  <div class="pill msg-label" style="top:168px;height:27px;width:83px">Key opportunities<br>of working with NLS</div>
  <div class="msg-box msg-box--opportunities" style="top:126px;height:112px">
    <b>Refinances</b>NLS runs switching for other clients with strong uptake and quick settlements once documents are returned. We would like to discuss doing the same for XYZ Lender and its customers.
    <b>Electronic Documents and Web Signing</b>NLS delivers documents and web signing online in New Zealand and is talking with other lenders here. NLS would like to help XYZ Lender set up the same.
    <b>Discharges</b>NLS would like to discuss handling discharges for XYZ Lender, drawing on close ties with all the major broker groups.
    <b>ECNL</b>NLS is working closely with ECNL for a smooth move to electronic conveyancing.
  </div>

  <div class="pill msg-label" style="top:240px;height:22px">Commitment<br>Sought</div>
  <div class="msg-box" style="top:242px;height:18px">NLS would like to work closely with XYZ Lender to improve its end to end mortgage processing.</div>

  <div class="confidential">COMMERCIAL IN CONFIDENCE</div>
</section>

<section class="slide slide--intro">
  <div class="pill section-pill">INTRODUCTION</div>
  <div class="company-name corner-name" style="left:266px">Northgate<br>Loan Services</div>
  <div class="col-title" style="left:11px;width:155px">ABOUT NORTHGATE LOAN SERVICES</div>
  <div class="col-title" style="left:198px;width:156px">NLS OFFICES</div>
  <div class="intro-text">
    <p>Northgate Loan Services (NLS) was established in NZ in 2001 and opened an office in Australia in 2004. In November 2007 NLS became a wholly owned subsidiary of Meridian Title Group and is the vehicle through which Meridian undertakes mortgage servicing in Australia and New Zealand.</p>
    <p>On 1 August 2012 NLS acquired Harbour Lenders Processing (HLP) to form one of the largest mortgage processing companies in Australasia.</p>
    <p>In providing services to the mortgage industry, NLS utilizes and deploys its existing resources and capability as well as the resources available to it through the Meridian family of companies internationally.</p>
    <p>NLS have approximately 300 staff operating in offices in Sydney, Melbourne, Adelaide, Brisbane, Perth and Auckland, refer map opposite.</p>
    <p>NLS undertakes approximately 150,000 settlements p.a.</p>
  </div>
  <div class="map-area" role="img" aria-label="Map of Australia and New Zealand marking offices in Perth, Adelaide, Melbourne, Sydney, Brisbane and Auckland"></div>
  <div class="confidential">COMMERCIAL IN CONFIDENCE</div>
</section>

<section class="slide slide--services">
  <div class="pill section-pill">SERVICE OFFERINGS</div>
  <div class="company-name corner-name" style="left:268px">Northgate<br>Loan Services</div>
  <div class="intro-note">
    <p>“Mortgage Servicing” can mean different things in different jurisdictions. For the purpose of this document we use it to refer to the full range of mortgage management and administration services during the period from receipt of instructions to prepare documents until repayment and discharge of the mortgage that can be outsourced by the lender to a third party.</p>
    <p style="margin-top:3px">The diagram below details the services provided by NLS.</p>
  </div>

  <div class="flow flow--loans">
    <span>Document Preparation</span><span>Verification</span><span>Bookings And Enquiries</span><span>Certification &amp; Settlement Preparation</span><span>Settlements</span><span>Stamping And Lodgement</span><span>Custody</span>
  </div>
  <div class="flow-notes flow-notes--loans">
    <ul><li>File creation</li><li>Complete / check title search</li><li>Check fees</li><li>Produce loan document pack</li><li>Forward documents to borrower</li></ul>
    <ul><li>Verify that executed documents are completed correctly signed and witnessed</li><li>Follow up on incomplete documents</li></ul>
    <ul><li>Contact the solicitor / conveyancer to book settlement</li><li>Contact outgoing lender to book settlement</li><li>Book settlement in settlement diary</li></ul>
    <ul><li>Send certification document to lender and request funds</li><li>Confirm funds and disbursements required at settlement</li><li>Issue cheques</li></ul>
    <ul><li>Complete final search</li><li>Collect bank cheques for settlement</li><li>Attend settlement</li><li>Confirm settlement and attend post settlement activities</li></ul>
    <ul><li>Stamping of documents</li><li>Lodgement of the documents with the relevant LTO</li></ul>
    <ul><li>Registered documents returned from LTO</li><li>Trail documents to the custodian</li></ul>
  </div>
  <div class="pill flow-tag" style="left:272px;top:150px;width:66px">New Loans</div>

  <div class="flow flow--discharges">
    <span>Document preparation</span><span>Bookings and enquiries</span><span>Advise payout figures</span><span>Prepare settlement instructions</span><span>Settlements</span><span>Custody</span>
  </div>
  <div class="flow-notes flow-notes--discharges">
    <ul><li>File creation</li><li>Check fees</li><li>Produce discharge documents and arrange execution by attorney</li><li>Forward letter to requesting party</li></ul>
    <ul><li>Book settlement in the settlement diary</li></ul>
    <ul><li>Receive the payout figure from the outgoing lender</li><li>Advise payout figure and any fees to the incoming lender</li></ul>
    <ul><li>Forward discharge documents and settlement instructions to effect settlement to applicable state office or settlement agent</li></ul>
    <ul><li>Attend settlement and collect funds to payout loan</li><li>Deposit cheques</li></ul>
    <ul><li>Trail any remaining documents from the security packet to the custodian</li></ul>
  </div>
  <div class="pill flow-tag" style="left:280px;top:250px;width:58px">Discharges</div>

  <div class="confidential">COMMERCIAL IN CONFIDENCE</div>
</section>

<section class="slide slide--closing">
  <div class="company-name">Northgate<br>Loan Services</div>
  <div class="thanks">Thank You<br>For Your Attention</div>
  <div class="contact">T: 123-456-0789<br>Street Name, City Name, State Zip Code</div>
  <div class="footer-url">www.northgatels.com</div>
</section>

</body>
</html>
```